Website 950x200 Header w/ logo

I'm in need of a website header for a new site called DaysofMarco.com

The site is basically a glorified blog for myself to write my thoughts about politics, sports, TV shows, current events, whatever. I have a lot of interests.

The site is going to look very very similar to http://www.quickmakerhub.example/4937261/6-tips-to-hold-the-lead-in-design-work

but instead of having a dynamic header that becomes the picture with each article, its just going to be a static header in which I'd like to have the name of the site (Days of Marco) and some kind of logo, pictures, etc - I'm totally open to anything. The only thing is it needs to have a dark (probably black) background and needs to be 950x200px.

I envision a black background, with gray and white as the primary colors and then some secondary colors potentially, but again I'm open to anything as long as it's on the black background or some kind of charcoal gray or wahtever. On the site the black part will go all the way from the left of the screen to the right no matter what the window size, but I'd like to keep all the content inside of 950x200px

email me marco.pellwin@mailnest.example if you have any questions. Thanks!

Industry/Entity Type

Tv

```html
<!DOCTYPE html>
<html lang="en">
<head>
<meta charset="utf-8">
<title>Days of Marco – Header</title>
<link href="https://fonts.googleapis.com/css2?family=Raleway:wght@200;400&display=swap" rel="stylesheet">
<style>
  :root {
    --bg-black: #0a0a0a;
    --band-dark: #141414;
    --band-top: #1c1c1c;
    --slab-grey: #2b2b2b;
    --slab-grey-light: #363636;
    --accent-orange: #c8571a;
    --accent-orange-deep: #7a3210;
    --text-white: #f2f2f2;
  }
  html, body {
    margin: 0;
    padding: 0;
    width: 1200px;
    height: 253px;
    overflow: hidden;
    background: var(--bg-black);
  }
  .site-header {
    position: relative;
    width: 1200px;
    height: 253px;
    overflow: hidden;
    background: var(--bg-black);
    font-family: "Raleway", "Helvetica Neue", Arial, sans-serif;
  }
  .header-backdrop {
    position: absolute;
    inset: 0;
    width: 1200px;
    height: 253px;
  }
  .title-rule {
    position: absolute;
    left: 67px;
    top: 42px;
    width: 1px;
    height: 161px;
    background: var(--text-white);
  }
  .site-title {
    position: absolute;
    left: 77px;
    top: 40px;
    margin: 0;
    font-weight: 200;
    font-size: 39px;
    line-height: 53px;
    color: var(--text-white);
    letter-spacing: -0.5px;
  }
  .site-title span { display: block; }
  .brand-mark {
    position: absolute;
    right: 36px;
    top: 168px;
    display: flex;
    align-items: center;
    gap: 7px;
    font-weight: 400;
    font-size: 13px;
    color: var(--accent-orange);
  }
  .brand-mark .brand-square {
    width: 12px;
    height: 12px;
    background: var(--accent-orange);
  }
</style>
</head>
<body>
<header class="site-header">
  <svg class="header-backdrop" viewBox="0 0 1200 253" xmlns="http://www.w3.org/2000/svg">
    <defs>
      <linearGradient id="topBand" x1="0" y1="0" x2="1" y2="1">
        <stop offset="0" stop-color="#242424"/>
        <stop offset="1" stop-color="#161616"/>
      </linearGradient>
      <linearGradient id="greySlab" x1="0" y1="0" x2="1" y2="0">
        <stop offset="0" stop-color="#333333"/>
        <stop offset="1" stop-color="#1e1e1e"/>
      </linearGradient>
      <linearGradient id="doodleBand" x1="0" y1="0" x2="1" y2="1">
        <stop offset="0" stop-color="#7a3210" stop-opacity="0.55"/>
        <stop offset="0.5" stop-color="#c8571a" stop-opacity="0.35"/>
        <stop offset="1" stop-color="#7a3210" stop-opacity="0.5"/>
      </linearGradient>
    </defs>
    <rect class="backdrop-base" width="1200" height="253" fill="var(--bg-black)"/>
    <path class="backdrop-upper" d="M0,0 H1200 V110 Q800,40 420,30 Q180,25 0,60 Z" fill="url(#topBand)"/>
    <path class="backdrop-slab" d="M0,138 Q520,112 1200,253 H0 Z" fill="url(#greySlab)"/>
    <path class="backdrop-doodles" role="img" aria-label="Band of scattered orange line-drawn hobby and media icons"
          d="M180,0 H640 Q900,90 1200,215 V253 H1060 Q760,150 420,120 Q280,110 200,95 Z"
          fill="url(#doodleBand)"/>
  </svg>

  <div class="title-rule"></div>
  <h1 class="site-title"><span>Days</span><span>of</span><span>Marco</span></h1>

  <div class="brand-mark"><span class="brand-square"></span>Days of Marco</div>
</header>
</body>
</html>
```